Wordpress and Elementor Pro website

We need a Wordpress/Elementor Pro design for our website. We already have a logo design and installed Wordpress. We have some ideas concerning the design, and we will share two websites. Both the design and content placement we like about these websites. We would like to see designs that use the color Purple (the same as the logo color), white and black. We provide these services: SEO optimization, SEO copywriting and online campaigns. We will provide a list of the page's we would like to see in the design.

Target Market(s)

Entrepreneurs, business owners. Companies who would like to expand online with texts and SEO.

Industry/Entity Type

Digital Marketing

Coding

Coded - Design and coding required

Number of Pages Required

5+ page

Font styles to use
Sans Serif

Colors
886aae
fffefd
0355a3

Requirements
Must have
• Single pages and singel posts of Elementor so I can create new pages and blog posts in the future.

```html
<!DOCTYPE html>
<html lang="en">
<head>
<meta charset="utf-8">
<title>Verdano – Digital Marketing</title>
<link rel="stylesheet" href="https://fonts.googleapis.com/css2?family=Open+Sans:wght@400;600;700&family=Roboto:wght@300;500;700&display=swap">
<style>
:root{
  --purple:#6a50b0;
  --purple-dark:#5a41a0;
  --lavender:#ebe6f4;
  --ink:#2b2b2b;
  --muted:#a3a3a3;
  --white:#ffffff;
  --navy:#201e3b;
  --navy-input:#3a3855;
}
*{margin:0;padding:0;box-sizing:border-box}
html,body{width:1200px;height:3836px;overflow:hidden}
body{font-family:"Open Sans",sans-serif;color:var(--ink);background:var(--white);position:relative}
section,header,footer{position:relative;width:1200px;overflow:hidden}
.abs{position:absolute}
.center{left:0;width:1200px;text-align:center}

/* top bar */
.topbar{height:45px;background:var(--purple);color:var(--white);font-size:14px}
.topbar span{position:absolute;top:13px;display:flex;align-items:center;gap:8px}

/* nav */
.nav{height:86px;background:var(--white)}
.brand{position:absolute;left:88px;top:12px;width:118px;text-align:center;color:var(--purple)}
.brand .mark{display:block;width:30px;height:30px;margin:0 auto 4px;border:2px solid var(--purple);border-radius:50%}
.brand .name{font-size:18px;letter-spacing:1px;font-weight:400}
.menu{position:absolute;left:356px;top:34px;display:flex;gap:21px;font-size:12px;font-weight:600;color:#444}
.menu .active{color:var(--purple)}
.socials{position:absolute;right:90px;top:34px;display:flex;gap:16px}
.socials i{width:14px;height:14px;background:#222;display:block;border-radius:2px}

/* hero */
.hero{height:557px}
.hero .photo{position:absolute;inset:0;background:linear-gradient(120deg,#3d4a57 0%,#6f7f8d 45%,#a6b2bc 75%,#5b6975 100%)}
.hero .shade{position:absolute;inset:0;background:rgba(20,25,35,.35)}
.hero h1{top:120px;font-family:"Roboto",sans-serif;font-size:50px;line-height:57px;color:var(--white);font-weight:300}
.hero h1 b{font-weight:700}
.hero .sub{top:273px;font-size:16px;color:var(--white)}
.btn{display:inline-block;background:var(--purple);color:var(--white);font-size:12px;font-weight:700;border-radius:24px;text-align:center;box-shadow:0 8px 16px rgba(90,65,160,.3)}
.hero .btn{position:absolute;left:439px;top:344px;width:162px;height:45px;line-height:45px;font-weight:500;font-family:"Roboto",sans-serif}
.play{position:absolute;left:618px;top:342px;display:flex;align-items:center;gap:12px;color:var(--white);font-size:12px;font-family:"Roboto",sans-serif}
.play .ring{width:50px;height:50px;border:2px solid var(--white);border-radius:50%;display:flex;align-items:center;justify-content:center}
.dots{position:absolute;left:572px;top:496px;display:flex;gap:9px}
.dots i{width:11px;height:11px;border-radius:50%;background:rgba(255,255,255,.5)}
.dots i:first-child{background:var(--white)}

/* shared headings */
.eyebrow{font-size:11px;color:var(--purple-dark);letter-spacing:.3px}
.title{font-size:32px;font-weight:400;color:var(--ink)}
.title em{font-style:normal;color:var(--purple)}
.lede{font-size:15px;line-height:24px;color:var(--muted)}

/* welcome */
.welcome{height:689px}
.welcome .eyebrow{top:110px}
.welcome .title{top:150px}
.welcome .lede{top:168px;left:250px;width:700px;top:168px}
.cards{position:absolute;left:92px;top:880px}
.card{position:absolute;top:880px;width:319px;height:256px;border:1px solid #eee;border-radius:8px;padding:38px 37px;background:var(--white)}
.card .num{font-size:45px;color:var(--purple);font-weight:400;line-height:50px}
.card h3{font-size:17px;font-weight:600;margin-top:12px;color:var(--ink)}
.card p{font-size:12.5px;line-height:24px;color:var(--muted);margin-top:10px}
.card.featured{border:none;color:var(--white);overflow:hidden}
.card.featured .bg{position:absolute;inset:0;background:linear-gradient(135deg,#6e6e74,#a9a7ab 55%,#4b4a55)}
.card.featured > *:not(.bg){position:relative;color:var(--white)}

/* about */
.about{height:593px;background:var(--lavender)}
.about .eyebrow{left:91px;top:118px}
.about .title{left:94px;top:152px;line-height:38px;font-size:32px}
.about .lede{left:91px;top:252px;width:490px;line-height:26px;font-size:14.5px}
.about .btn{position:absolute;left:91px;top:410px;width:159px;height:45px;line-height:45px}
.about .back{position:absolute;left:645px;top:149px;width:464px;height:334px;background:var(--purple);border-radius:8px}
.about .pic{position:absolute;left:613px;top:110px;width:467px;height:336px;border-radius:6px;background:linear-gradient(160deg,#f2f1f4,#c9c8cf 45%,#3a3a44 70%,#d8d7db);box-shadow:0 10px 24px rgba(0,0,0,.15)}

/* customers */
.customers{height:546px;background:var(--purple)}
.customers .photo{position:absolute;inset:0;background:linear-gradient(110deg,#7560b8 0%,#8a78c4 40%,#6750b0 70%,#7a68bd 100%);opacity:.9}
.customers .eyebrow{top:118px;color:var(--white)}
.customers .title{top:150px;color:var(--white);font-size:30px}
.customers .lede{top:204px;left:250px;width:700px;color:var(--white)}
.partners{position:absolute;left:160px;top:345px;display:flex;gap:95px}
.partners i{width:64px;height:64px;background:var(--white);display:block;border-radius:50%;opacity:.95}
.partners i:nth-child(2n){border-radius:6px}
.arrow{position:absolute;top:362px}

/* services */
.services{height:648px}
.services .eyebrow{top:119px}
.services .title{top:158px}
.services .lede{top:212px;left:250px;width:700px}
.service{position:absolute;top:327px;width:320px;text-align:center}
.service .icon{width:80px;height:80px;border-radius:50%;background:var(--lavender);margin:0 auto;display:flex;align-items:center;justify-content:center}
.service h4{font-size:17px;font-weight:600;margin-top:20px}
.service p{font-size:12.5px;line-height:26px;color:var(--muted);margin-top:12px}

/* cta */
.cta{height:238px;background:var(--lavender)}
.cta .eyebrow{left:91px;top:68px}
.cta .title{left:94px;top:106px;line-height:38px}
.cta .btn{position:absolute;left:871px;top:116px;width:159px;height:45px;line-height:45px}

/* footer */
.footer{height:434px;background:var(--navy);color:var(--white)}
.footer .brand{left:92px;top:80px}
.footer .about-text{left:92px;top:166px;width:215px;font-size:11.5px;line-height:25px}
.footer .social{left:92px;top:288px;display:flex;gap:18px}
.footer .social i{width:11px;height:11px;background:var(--white);border-radius:2px;display:block}
.footer h5{font-size:15px;font-weight:600;font-family:"Roboto",sans-serif}
.contact-list{list-style:none;font-size:11.5px;line-height:29px}
.contact-list li{display:flex;align-items:center;gap:13px}
.links{list-style:none;font-size:11.5px;line-height:29px}
.newsletter .input{width:223px;height:36px;border-radius:18px;background:var(--navy-input);font-size:11.5px;padding:11px 18px}
.newsletter .sub-btn{width:137px;height:34px;border:1px solid var(--purple);border-radius:18px;color:var(--purple);font-size:12px;text-align:center;line-height:32px;margin-top:21px}
.footer .rule{left:92px;top:350px;width:1002px;height:1px;background:#3b3960}
.footer .copy{top:380px;font-size:11.5px}
</style>
</head>
<body>

<header class="topbar">
  <span style="left:86px">
    <svg width="18" height="12" viewBox="0 0 18 12"><rect x="1" y="1" width="16" height="10" fill="none" stroke="#fff" stroke-width="1.5"/><path d="M1 1l8 6 8-6" fill="none" stroke="#fff" stroke-width="1.5"/></svg>
    hello@verdano.com
  </span>
  <span style="left:328px">
    <svg width="14" height="14" viewBox="0 0 14 14"><path d="M3 1l3 3-1.5 1.5a8 8 0 004 4L10 8l3 3-2 2C6 13 1 8 1 3z" fill="#fff"/></svg>
    201 5550-123-45
  </span>
</header>

<header class="nav">
  <div class="brand"><span class="mark"></span><span class="name">VERDANO</span></div>
  <nav class="menu">
    <span class="active">HOME</span><span>ABOUT</span><span>SERVICE</span><span>TEAM</span><span>PORTFOLIO</span><span>PRICE</span><span>BLOG</span><span>CONTACT</span>
  </nav>
  <div class="socials"><i></i><i></i><i></i></div>
</header>

<section class="hero">
  <div class="photo" role="img" aria-label="Man working on a laptop on a leather sofa by a large city-view window"></div>
  <div class="shade"></div>
  <h1 class="abs center"><b>OMDAT ONLINE GROEIEN</b> IN OMZET<br>EN WINST EEN SPECIALISME IS</h1>
  <p class="abs center sub">Experience To Give You Better Results</p>
  <span class="btn">GET STARTED</span>
  <div class="play">
    <span class="ring"><svg width="16" height="18" viewBox="0 0 16 18"><path d="M2 1l13 8-13 8z" fill="#fff"/></svg></span>
    START VIDEO
  </div>
  <div class="dots"><i></i><i></i><i></i></div>
</section>

<section class="welcome">
  <p class="abs center eyebrow">WELCOME TO VERDANO</p>
  <h2 class="abs center title">ALL YOU NEED FOR <em>YOUR BUSINESS</em></h2>
  <p class="abs lede" style="top:211px;text-align:center">Lorem ipsum dolor sit amet, consectetur adipiscing elit, sed do eiusmod tempor incididunt ut lab ore et dolore magna aliqua. Ut enim ad minim veniam.</p>

  <article class="card" style="left:92px;top:322px">
    <div class="num">01</div>
    <h3>SEO OPTIMIZATION</h3>
    <p>Lorem ipsum dolor sit amet, consecte tur adipiscing elit, sed do eiusmod te mpor incididunt ut lab ore et d.</p>
  </article>
  <article class="card featured" style="left:439px;top:322px">
    <div class="bg" role="img" aria-label="Woman working on a laptop on a sofa"></div>
    <div class="num">02</div>
    <h3>SEO COPYWRITING</h3>
    <p>Lorem ipsum dolor sit amet, consecte tur adipiscing elit, sed do eiusmod te mpor incididunt ut lab ore et d.</p>
  </article>
  <article class="card" style="left:786px;top:322px">
    <div class="num">03</div>
    <h3>ONLINE CAMPAIGNS</h3>
    <p>Lorem ipsum dolor sit amet, consecte tur adipiscing elit, sed do eiusmod te mpor incididunt ut lab ore et d.</p>
  </article>
</section>

<section class="about">
  <p class="abs eyebrow">ABOUT US</p>
  <h2 class="abs title">ALL YOU NEED FOR<br><em>YOUR BUSINESS</em></h2>
  <p class="abs lede">Lorem ipsum dolor sit amet, consectetur adipiscing elit, sed do eiusmod tempor incididunt ut lab ore et dolore magna aliqua. Ut enim ad mi nim veniam.Lorem ipsum dolor sit amet, consectetur adipiscing elit, d tempor incididunt ut lab ore et dolore magna aliqua. Ut enim ad mi nim veniam.NNN</p>
  <span class="btn">READ MORE</span>
  <div class="back"></div>
  <div class="pic" role="img" aria-label="Laptop showing a design portfolio on a desk with a plant and a mug"></div>
</section>

<section class="customers">
  <div class="photo" role="img" aria-label="Man at a laptop behind a purple overlay"></div>
  <p class="abs center eyebrow">OUR CUSTOMERS</p>
  <h2 class="abs center title">THESE ARE SOME OF OUR CUSTOMERS</h2>
  <p class="abs lede" style="text-align:center">Lorem ipsum dolor sit amet, consectetur adipiscing elit, sed do eiusmod tempor incididunt ut lab ore et dolore magna aliqua. Ut enim ad minim veniam.</p>
  <svg class="arrow" style="left:86px" width="20" height="30" viewBox="0 0 20 30"><path d="M16 3L5 15l11 12" fill="none" stroke="#fff" stroke-width="4"/></svg>
  <div class="partners"><i></i><i></i><i></i><i></i><i></i><i></i></div>
  <svg class="arrow" style="left:1086px" width="20" height="30" viewBox="0 0 20 30"><path d="M4 3l11 12L4 27" fill="none" stroke="#fff" stroke-width="4"/></svg>
</section>

<section class="services">
  <p class="abs center eyebrow">OUR SERVICES</p>
  <h2 class="abs center title">OUR AMAZING <em>SERVICES</em></h2>
  <p class="abs lede" style="text-align:center">Lorem ipsum dolor sit amet, consectetur adipiscing elit, sed do eiusmod tempor incididunt ut lab ore et dolore magna aliqua. Ut enim ad minim veniam.</p>

  <div class="service" style="left:90px">
    <div class="icon"><svg width="34" height="34" viewBox="0 0 34 34"><circle cx="17" cy="12" r="8" fill="#6a50b0"/><path d="M3 32c1-9 7-12 14-12s13 3 14 12z" fill="#6a50b0"/></svg></div>
    <h4>CUSTOMER SERVICE</h4>
    <p>Lorem ipsum dolor sit amet, consectetur adipiscin g elit, sed do eiusmod tempor incididunt ut lab KJHore et d.</p>
  </div>
  <div class="service" style="left:440px">
    <div class="icon"><svg width="34" height="34" viewBox="0 0 34 34"><circle cx="13" cy="20" r="8" fill="none" stroke="#6a50b0" stroke-width="5"/><circle cx="25" cy="9" r="5" fill="none" stroke="#6a50b0" stroke-width="4"/></svg></div>
    <h4>GREAT RESULTS</h4>
    <p>Lorem ipsum dolor sit amet, consectetur adipiscin g elit, sed do eiusmod tempor incididunt ut lab KJHore et d.</p>
  </div>
  <div class="service" style="left:790px">
    <div class="icon"><svg width="34" height="34" viewBox="0 0 34 34"><rect x="5" y="18" width="6" height="12" fill="#6a50b0"/><rect x="14" y="11" width="6" height="19" fill="#6a50b0"/><rect x="23" y="4" width="6" height="26" fill="#6a50b0"/></svg></div>
    <h4>YEARS OF EXPERIENCE</h4>
    <p>Lorem ipsum dolor sit amet, consectetur adipiscin g elit, sed do eiusmod tempor incididunt ut lab KJHore et d.</p>
  </div>
</section>

<section class="cta">
  <p class="abs eyebrow">ABOUT US</p>
  <h2 class="abs title">LET’S TALK ABOUT WHAT WE CAN DO FOR<br><em>YOUR BUSINESS</em></h2>
  <span class="btn">READ MORE</span>
</section>

<footer class="footer">
  <div class="brand" style="color:#fff"><span class="mark" style="border-color:#fff"></span><span class="name">VERDANO</span></div>
  <p class="abs about-text">Lorem ipsum dolor sit amet, consectetur adipiscing elit, sed do eiusmod tempor incididunt ut labore et dolore magna aliqua. Ut enim ad minim veniam,</p>
  <div class="abs social"><i></i><i></i><i></i><i></i></div>

  <div class="abs" style="left:353px;top:96px">
    <h5>Contacts</h5>
    <ul class="contact-list" style="margin-top:30px">
      <li><svg width="14" height="14"><circle cx="7" cy="7" r="6" fill="#6a50b0"/></svg>Mon - Fri: 8.00am to 6.00pm</li>
      <li><svg width="14" height="14" viewBox="0 0 14 14"><path d="M7 1a4.5 4.5 0 014.5 4.5C11.5 9 7 13 7 13S2.5 9 2.5 5.5A4.5 4.5 0 017 1z" fill="#6a50b0"/></svg>88 Canal Lane, Netherlands</li>
      <li><svg width="14" height="14" viewBox="0 0 14 14"><path d="M3 1l3 3-1.5 1.5a8 8 0 004 4L10 8l3 3-2 2C6 13 1 8 1 3z" fill="#6a50b0"/></svg>+121 555-010-200</li>
      <li><svg width="14" height="14" viewBox="0 0 14 14"><rect x="1" y="3" width="12" height="8" fill="#6a50b0"/></svg>info@verdano.com</li>
    </ul>
  </div>

  <div class="abs" style="left:610px;top:94px">
    <h5>Useful Links</h5>
    <div style="display:flex;gap:58px;margin-top:30px">
      <ul class="links"><li>Cases</li><li>About Us</li><li>Contact Us</li><li>Services</li></ul>
      <ul class="links"><li>Cookie Policy</li><li>Exclaimer</li><li>Privacy Policy</li></ul>
    </div>
  </div>

  <div class="abs newsletter" style="left:874px;top:104px">
    <h5>Newsletter</h5>
    <div class="input" style="margin-top:22px">Your email...</div>
    <div class="sub-btn">Subscribe</div>
  </div>

  <div class="abs rule"></div>
  <p class="abs center copy">VERDANO SPECIALISTEN</p>
</footer>

</body>
</html>
```